Cookie needs a website

We need a website for a cookie company based in Mexico City. Our company (called Panes Doradillos) has been baking and crating all sorts of cookies and cakes for more than 35 years.
We started off as a family business and till this date we are still functioning as one. We need the design of the web to be more on the baking side as we have many types of cookies cakes, pastries & muffins. Key elements, home style baking, use colours black, white and red. Tabs we need: front page, who are we, our brands and contact Preferable in Spanish. Im sure you have questions, please contact us. This is for homepage PSD design only no CSS,XHTML or full website build or coding involved as this is design competition.
Updates

Some more information has been added. Thanks is advance for your talent!

Target Market(s)

Target is general public, mostly families. Our product is not a luxury good,more like an affordable treat, however we do use very high quality products and high quality standards. Our motive is natural ingredients and home baked goods.
Our main point of sales is having shops inside department stores. Our own shops and selling to other businesses for re sale

Industry/Entity Type

Business

Font styles to use
Serif

Colors
ec2027
ffffff
333333

Requirements
Must have
• Baking oriented. An oven would be nice since we bake in front of our clients.
Colors we use also important
Nice to have
• make it home. (you have design freedom)
Below are the logos PD is the company name. Tomelo is one of our branches and the the pictures are from the cookies we make
Should not have
• PLEASE NO corny, over colorfull or tacky designs!!

```html
<!DOCTYPE html>
<html lang="es">
<head>
<meta charset="utf-8">
<title>Panes Doradillos</title>
<link href="https://fonts.googleapis.com/css2?family=Lobster&family=Open+Sans:wght@400;600&family=Oswald:wght@300;400&display=swap" rel="stylesheet">
<style>
:root{
  --red:#dc2229;
  --red-dark:#b81c22;
  --ink:#333333;
  --paper:#f4f2ef;
  --white:#ffffff;
  --wood-dark:#2a1108;
  --wood:#5a2512;
  --wood-light:#7a3418;
  --black:#111111;
  --gold:#f2a81d;
}
*{box-sizing:border-box;margin:0;padding:0}
html,body{width:806px;height:1200px;overflow:hidden}
body{position:relative;background:var(--paper);font-family:"Open Sans",sans-serif;color:var(--ink)}
.abs{position:absolute}
.script{font-family:"Lobster",cursive;font-weight:400}

.top-wood{left:0;top:0;width:806px;height:276px;background:linear-gradient(90deg,var(--wood-dark),var(--wood) 20%,var(--wood-light) 50%,var(--wood) 80%,var(--wood-dark))}
.top-wood::after{content:"";position:absolute;left:0;bottom:-4px;width:100%;height:6px;background:radial-gradient(circle at 50% 100%,var(--paper) 3px,transparent 3.5px) 0 0/7px 6px repeat-x}
.foot-wood{left:0;top:920px;width:806px;height:238px;background:linear-gradient(90deg,var(--wood-dark),var(--wood) 25%,var(--wood-light) 50%,var(--wood) 75%,var(--wood-dark))}
.foot-wood::before{content:"";position:absolute;left:0;top:-2px;width:100%;height:6px;background:radial-gradient(circle at 50% 0,var(--paper) 3px,transparent 3.5px) 0 0/7px 6px repeat-x}

.ribbon{left:66px;top:53px}
.nav{left:106px;top:53px;width:632px;height:43px;display:flex;align-items:center}
.nav a{font-family:"Lobster",cursive;color:var(--red);font-size:13px;text-decoration:none;text-align:center}
.nav .left{display:flex;width:236px;justify-content:space-around}
.nav .right{display:flex;width:236px;margin-left:auto;justify-content:space-around}

.brand{left:342px;top:0;width:122px;height:138px;background:var(--black);color:var(--white);text-align:center;font-family:"Oswald",sans-serif;font-weight:300;box-shadow:0 2px 6px rgba(0,0,0,.5)}
.brand .mono{display:block;font-size:44px;line-height:1;margin-top:24px;letter-spacing:2px}
.brand .name{display:block;font-size:12.5px;margin-top:16px}

.slider{left:114px;top:109px;width:577px;height:289px;background:var(--white);box-shadow:0 8px 10px -6px rgba(0,0,0,.45)}
.slide-photo{left:6px;top:5px;width:566px;height:279px;background:radial-gradient(ellipse at 60% 40%,#a77a4e,#5a3320 55%,#2a1610)}
.slide-label{left:6px;top:119px;width:241px;height:50px;background:rgba(210,34,41,.88);color:var(--white);font-size:31px;line-height:50px;padding-left:12px}
.slide-next{left:540px;top:138px;width:24px;height:24px;border-radius:50%;background:var(--black);border:1.5px solid #555}

.welcome{left:0;top:418px;width:806px;text-align:center;font-size:21px;color:#2b2b2b}
.intro{left:118px;top:456px;width:570px;text-align:center;font-size:8.3px;line-height:13.6px;color:#555}

.card{top:515px;width:181px;height:164px;background:var(--white);border:1px solid #e3e0dc}
.card .photo{left:4px;top:4px;width:171px;height:117px}
.card .bar{left:4px;top:121px;width:171px;height:38px;background:var(--red);color:var(--white);display:flex;align-items:center;justify-content:space-between;padding:0 12px}
.card .bar span{font-family:"Lobster",cursive;font-size:14px}
.card .bar i{font-style:normal;font-size:7px;color:var(--gold);letter-spacing:1px}
.card .bar i b{color:var(--white);font-weight:400}

.divider{left:114px;top:714px;width:577px;height:4px}
.divider::before,.divider::after{content:"";position:absolute;top:0;width:260px;border-top:1px solid #d8d0b8;border-bottom:1px solid #d8d0b8;height:3px}
.divider::before{left:0}.divider::after{right:0}
.divider .knot{left:270px;top:-4px;width:37px;height:11px;border:1px solid #cfc4a5;border-radius:50%}

.events-title{left:114px;top:732px;font-size:17px;color:#222}
.event-photo{left:114px;top:770px;width:110px;height:112px;background:linear-gradient(135deg,#3a3a3a,#9a9a9a 50%,#d7d4cf)}
.event-body{left:242px;top:767px;width:195px}
.event-body h3{font-weight:400;font-size:11px;color:#444}
.event-body .stars{margin-top:6px;font-size:8px;color:var(--gold)}
.event-body .stars em{font-style:normal;color:#bbb}
.event-body .stars span{color:#555;margin-left:12px;font-size:7.5px}
.event-body p{margin-top:7px;font-size:7px;line-height:12.8px;color:#777}
.event-body .more{display:block;margin-top:4px;font-size:6.5px;color:#444;text-decoration:none}
.event-body .more b{color:var(--gold)}

.recipes{left:449px;top:743px;width:241px;height:142px;background:linear-gradient(90deg,#321610 0%,#3a1a12 45%,#6c4428 75%,#3b2014)}
.recipes h3{position:absolute;left:16px;top:18px;font-family:"Lobster",cursive;font-weight:400;font-size:19px;color:var(--white)}
.recipes p{position:absolute;left:17px;top:54px;width:100px;font-size:7px;line-height:12.8px;color:#ddd}
.recipes .btn{position:absolute;left:17px;top:104px;width:55px;height:20px;background:var(--red);color:var(--white);font-size:7.5px;line-height:20px;text-align:center;border-radius:2px}

.contact{left:115px;top:948px;color:var(--white)}
.contact h2{font-family:"Oswald",sans-serif;font-weight:400;font-size:17px;color:#cfc6c0;letter-spacing:.3px}
.contact .item{position:absolute;left:0;width:200px}
.contact .item svg{position:absolute;left:0;top:0}
.contact h4{margin-left:28px;font-family:"Open Sans",sans-serif;font-weight:400;font-size:10px;letter-spacing:.3px}
.contact p{margin-left:28px;font-size:8.5px;line-height:13.6px;color:#e4d8d0;margin-top:5px}

.form{left:318px;top:949px;width:225px}
.form .field{position:absolute;left:0;width:225px;height:25px;border:1px solid #d8c8c0;border-radius:3px;color:var(--white);font-size:8px;padding:7px 9px}
.form .send{position:absolute;left:0;top:161px;width:76px;height:20px;background:var(--red);color:var(--white);font-size:8px;line-height:20px;text-align:center;border-radius:2px}

.partner{left:577px;top:954px;width:114px;height:96px;background:var(--white);display:flex;align-items:center;justify-content:center;font-family:"Open Sans",sans-serif;font-weight:600;font-size:18px;color:var(--black)}
.social{left:577px;top:1063px;display:flex;gap:3px}
.social span{width:20px;height:20px;border:1px solid #e5d8d0;border-radius:50%}

.bottom{left:0;top:1158px;width:806px;height:42px;background:var(--black)}
.bottom .name{position:absolute;left:128px;top:11px;font-size:14px;color:#ddd;font-weight:400}
.bottom .name b{display:inline-block;width:12px;height:12px;border:1px solid #ddd;border-radius:50%;margin-right:10px;vertical-align:-1px}
.bottom nav{position:absolute;left:487px;top:16px;font-size:7.5px;color:#ddd}
.bottom nav a{color:#ddd;text-decoration:none}
</style>
</head>
<body>

<div class="abs top-wood" role="img" aria-label="Dark wooden plank background"></div>

<svg class="abs ribbon" width="674" height="50" viewBox="0 0 674 50" aria-hidden="true">
  <polygon points="0,6 40,6 40,46 0,46 14,26" fill="#ece8e2"/>
  <polygon points="674,6 634,6 634,46 674,46 660,26" fill="#ece8e2"/>
  <rect x="40" y="0" width="594" height="43" fill="#f4f1ec" stroke="#ddd6cc"/>
  <line x1="40" y1="4" x2="634" y2="4" stroke="#cfc7bb" stroke-dasharray="2 2"/>
  <line x1="40" y1="39" x2="634" y2="39" stroke="#cfc7bb" stroke-dasharray="2 2"/>
</svg>
<nav class="abs nav">
  <div class="left"><a href="#">Home</a><a href="#">About</a><a href="#">Special Events</a></div>
  <div class="right"><a href="#">Menu</a><a href="#">Contact</a><a href="#">Recipes</a></div>
</nav>
<div class="abs brand"><span class="mono">PD</span><span class="name">Panes Doradillos</span></div>

<div class="abs slider">
  <div class="abs slide-photo" role="img" aria-label="Close-up photo of broken nut and chocolate cookies"></div>
  <div class="abs slide-label script">Cookies &amp; Cakes</div>
  <div class="abs slide-next"><svg width="21" height="21" viewBox="0 0 21 21"><path d="M9 6l5 4.5-5 4.5" stroke="#fff" stroke-width="2" fill="none"/></svg></div>
</div>

<h1 class="abs welcome script">Welcome To Panes Doradillos</h1>
<p class="abs intro">Lorem ipsum dolor sit amet, consectur vesta elit. Nullam ornare tortor eget mi mattis moro sed non ipsum. Maecenas porta justo nonna ipiscing dapibus vel sed mi. Phasellus malvel in dui vehicula condimetm. Phasellus digtat. elit. Lorem ipsum dolor sit amet.Lorem ipsum dolor sit amet, consectur vesta elit. Nullam ornare tortor eget mi mattis moro sed non ipsum. Maecenas porta justo nonna</p>

<div class="abs card" style="left:114px">
  <div class="abs photo" role="img" aria-label="Photo of sugar cookies on a baking tray" style="background:linear-gradient(160deg,#3a2a1c,#d8a55c 45%,#e8c07a)"></div>
  <div class="abs bar"><span>Cookies</span><i>★★★<b>★★</b></i></div>
</div>
<div class="abs card" style="left:312px">
  <div class="abs photo" role="img" aria-label="Photo of fruit tarts and small cakes" style="background:linear-gradient(160deg,#6a4a30,#c9a070 45%,#4a2a1a)"></div>
  <div class="abs bar"><span>Cakes</span><i>★★★<b>★★</b></i></div>
</div>
<div class="abs card" style="left:510px">
  <div class="abs photo" role="img" aria-label="Photo of a stack of chocolate chip cookies" style="background:linear-gradient(160deg,#5a3a2a,#b88a5e 50%,#7a5a40)"></div>
  <div class="abs bar"><span>Special Discount</span><i>★★★<b>★★</b></i></div>
</div>

<div class="abs divider"><div class="abs knot"></div></div>

<h2 class="abs events-title script">Special Events</h2>
<div class="abs event-photo" role="img" aria-label="Photo of a stand mixer with a steel bowl"></div>
<div class="abs event-body">
  <h3>Sed ut perspiciatis unde omnis</h3>
  <div class="stars">★★★<em>★★</em><span>3967 reviews</span></div>
  <p>Sed egestas, ante et vulputate volutpat, eros pede semper vitae luctus metus libero eu augue. Morbi purus libero, faucibus adipiscing, commodo quis, gravida id, est. Sed lectus. Praesent elementum&nbsp; Sed egestas, ante et vulputate volutpat, eros pede semper</p>
  <a class="more" href="#">LEARN MORE &nbsp;<b>➔</b></a>
</div>

<div class="abs recipes" role="img" aria-label="Recipes banner with a photo of broken cookies">
  <h3>Recipes</h3>
  <p>Lorem ipsum dolor sit amet, consete adipiscing elituis eros</p>
  <span class="btn">Shop Now</span>
</div>

<div class="abs foot-wood" role="img" aria-label="Warm wooden plank background"></div>

<div class="abs contact">
  <h2>CONTACT US</h2>
  <div class="item" style="top:34px">
    <svg width="10" height="13" viewBox="0 0 10 13"><path d="M5 0a4.5 4.5 0 0 0-4.5 4.5C.5 8 5 13 5 13s4.5-5 4.5-8.5A4.5 4.5 0 0 0 5 0zm0 6.3a1.8 1.8 0 1 1 0-3.6 1.8 1.8 0 0 1 0 3.6z" fill="#fff"/></svg>
    <h4>ADDRESS</h4>
    <p>Calle Olivo 142<br>Colonia Roma Norte, CDMX 06700</p>
  </div>
  <div class="item" style="top:92px">
    <svg width="12" height="12" viewBox="0 0 12 12"><path d="M2.4 0l2 2.6-1.2 1.6c.7 1.6 2.1 3 3.7 3.7l1.6-1.2L11 8.7 9.7 11C5 11 0 6 0 1.3z" fill="#fff"/></svg>
    <h4>CALL US</h4>
    <p style="font-size:10px">+52 55-4812-3096</p>
  </div>
  <div class="item" style="top:144px">
    <svg width="14" height="11" viewBox="0 0 14 11"><rect x=".7" y=".7" width="12.6" height="9.6" rx="1" fill="none" stroke="#fff" stroke-width="1.3"/><path d="M1 1.5l6 4.5 6-4.5" fill="none" stroke="#fff" stroke-width="1.3"/></svg>
    <h4>E - MAIL</h4>
    <p style="margin-top:8px">hola@panesdoradillos.com</p>
  </div>
</div>

<div class="abs form">
  <div class="field" style="top:0">Name</div>
  <div class="field" style="top:32px">Email</div>
  <div class="field" style="top:64px">Phone</div>
  <div class="field" style="top:96px;height:56px">Message</div>
  <div class="send">SEND MESSAGE</div>
</div>

<div class="abs partner">Tomelo</div>
<div class="abs social" aria-label="Social links"><span></span><span></span><span></span><span></span><span></span></div>

<footer class="abs bottom">
  <span class="name"><b></b>Panes Doradillos</span>
  <nav><a href="#">Home</a> &nbsp;/&nbsp; <a href="#">Menu</a> &nbsp;/&nbsp; <a href="#">About</a> &nbsp;/&nbsp; <a href="#">Special events</a> &nbsp;/&nbsp; <a href="#">Reviews</a></nav>
</footer>

</body>
</html>
```